CoralPeak Travel

We are new traveling company from Italy and looking for a really unique design as soon as possible of the main page.
Travel is an online business. We all do online research before taking a vacation. Since some of us will spend hours researching a trip before finally booking it on a travel website, design is critical.
People looking to travel are going to start with an idea. Some may be browsing for a specific type of trip (river cruise, kayaking, etc.) while others may be looking at specific dates (i.e. February). Still others are considering going to a specific destination such as the Grand Canyon, but all of these visitors are goal-oriented. This type of visitor is frustrated by not finding thle right information easily. This is why travel web design must offer several ways to navigate such as by date, location, activity, cost, etc.
The design should be easy to use for visitors, look fantastic and be easy to update and maintain.
Uploaded some sample pictures but feel free to use your own if it looks good. About colors, blue and white would mix great.

Our future address will be coralpeaktravel.com

```html
<!DOCTYPE html>
<html lang="en">
<head>
<meta charset="utf-8">
<title>CoralPeak Travel</title>
<link rel="stylesheet" href="https://fonts.googleapis.com/css2?family=Roboto+Condensed:wght@400;700&family=Arimo:ital,wght@0,400;0,700;1,400&display=swap">
<style>
:root{
  --brand-blue:#2350a0;
  --title-blue:#1e4fa0;
  --bar-dark:#25272b;
  --search-cyan:#2aa8c8;
  --card-blue:#0f6bb8;
  --card-orange:#f0692a;
  --card-green:#62aa18;
  --band-green:#5ea615;
  --grey-bg:#e8e5e5;
  --text:#555a60;
  --white:#ffffff;
  --rule:#dcdcdc;
}
*{box-sizing:border-box;margin:0;padding:0}
html,body{width:1200px;height:2372px;overflow:hidden}
body{position:relative;background:var(--white);font-family:"Arimo",Arial,sans-serif;color:var(--text)}
.abs{position:absolute}
.center{left:0;width:1200px;text-align:center}
.cond{font-family:"Roboto Condensed",Arial,sans-serif}

/* hero */
.hero{top:0;left:0;width:1200px;height:571px;
  background:linear-gradient(180deg,#2f6fb8 0%,#6aa6d8 22%,#4f8a5a 36%,#3fa9b0 50%,#25c3c9 70%,#19b3c0 100%)}
.brand{top:38px;left:174px;font-family:"Roboto Condensed",Arial,sans-serif;font-weight:700;font-size:34px;color:var(--white)}
.nav{top:47px;font-family:"Arimo",Arial,sans-serif;font-size:15px;color:var(--white)}
.hero-title{top:203px;font-family:"Roboto Condensed",Arial,sans-serif;font-weight:700;font-size:46px;color:var(--white);letter-spacing:1px}
.hero-sub{top:266px;font-family:"Arimo",Arial,sans-serif;font-size:21px;line-height:34px;color:var(--white);text-shadow:0 1px 2px rgba(0,0,0,.4)}
.btn{background:var(--brand-blue);color:var(--white);font-family:"Roboto Condensed",Arial,sans-serif;font-size:20px;display:flex;align-items:center;justify-content:center}
.hero-arrow{top:257px;width:48px;height:48px;border:2px solid rgba(255,255,255,.7);border-radius:50%}

/* search */
.search{top:571px;left:0;width:1200px;height:110px;background:var(--bar-dark)}
.search-title{top:592px;left:174px;font-family:"Roboto Condensed",Arial,sans-serif;font-size:17px;color:var(--white)}
.field{top:628px;width:163px;height:28px;border:1px solid #cfd2d6;color:var(--white);font-size:11px;padding:0 12px;display:flex;align-items:center;justify-content:space-between}
.search-btn{top:628px;left:892px;width:136px;height:30px;background:var(--search-cyan);color:var(--white);font-size:12px;display:flex;align-items:center;justify-content:center}

/* sections */
.sec-title{font-family:"Roboto Condensed",Arial,sans-serif;font-size:22px;color:var(--title-blue)}
.para{left:210px;width:780px;text-align:center;font-size:12.5px;line-height:25px;color:var(--text)}
.rule{top:944px;left:0;width:1200px;height:2px;background:var(--rule)}

.card{top:1091px;width:273px;height:267px;color:var(--white);text-align:center}
.card h3{font-family:"Roboto Condensed",Arial,sans-serif;font-size:20px;font-weight:700;margin-top:34px}
.card p{font-size:11px;line-height:20px;margin:16px 28px 0}
.badge{top:1302px;width:112px;height:112px;border-radius:50%;background:var(--white);border:8px solid}

.testimonials{top:1469px;left:0;width:1200px;height:436px;background:var(--grey-bg)}
.t-card{top:1655px;width:412px;height:182px;background:var(--brand-blue);color:var(--white)}
.t-photo{top:0;left:0;width:208px;height:182px}
.t-body{top:30px;left:226px;width:170px}
.t-name{font-family:"Roboto Condensed",Arial,sans-serif;font-weight:700;font-size:13px}
.t-date{font-style:italic;font-size:11px;margin-top:9px}
.t-text{font-style:italic;font-size:11px;line-height:20px;margin-top:8px}
.t-arrow{top:1728px;font-size:28px;color:#8a8a8a;font-family:"Arimo",Arial,sans-serif}

.contact{top:1905px;left:0;width:1200px;height:70px;background:var(--band-green)}
.contact-text{top:1930px;left:171px;color:var(--white);font-size:12px}
.contact-text b{font-family:"Roboto Condensed",Arial,sans-serif;font-size:16px;font-style:normal}
.contact-text i{font-size:12px}
.contact-btn{top:1922px;left:876px;width:153px;height:35px;border:1px solid var(--white);color:var(--white);font-family:"Roboto Condensed",Arial,sans-serif;font-size:16px;display:flex;align-items:center;justify-content:center}

.news{top:1975px;left:0;width:1200px;height:397px;
  background:linear-gradient(180deg,#ffffff 0%,#ffffff 12%,#cdeff4 30%,#6fcfe0 55%,#4ab9d2 80%,#5ec3d8 100%)}
.news-para{left:170px;width:860px;text-align:center;font-size:11.5px;line-height:24px;text-transform:uppercase;color:#5d6470}
.email{top:2122px;left:392px;width:277px;height:30px;background:var(--white);font-size:11px;color:#9aa;padding:0 20px;display:flex;align-items:center}
.subscribe{top:2122px;left:688px;width:120px;height:30px;background:var(--brand-blue);color:var(--white);font-size:12px;font-weight:700;display:flex;align-items:center}
.subscribe .ic{width:34px;height:30px;border-right:1px solid rgba(255,255,255,.35);display:flex;align-items:center;justify-content:center}
.subscribe span{padding-left:14px}
.social{top:2191px;width:44px;height:44px;border-radius:50%}
.foot-rule{top:2272px;left:171px;width:858px;height:1px;background:rgba(255,255,255,.55)}
.copyright{top:2291px;font-size:11px;color:#2c4a7a}
</style>
</head>
<body>

<!-- Hero -->
<div class="abs hero" role="img" aria-label="Tropical lagoon with overwater bungalows, green mountains and palm leaves under a blue sky"></div>
<div class="abs brand">CoralPeak Travel</div>
<div class="abs nav" style="left:563px">Home</div>
<div class="abs nav" style="left:680px">About us</div>
<div class="abs nav" style="left:817px">Services</div>
<div class="abs nav" style="left:952px">Contact Us</div>

<div class="abs hero-arrow" style="left:66px">
  <svg width="44" height="44" viewBox="0 0 44 44"><path d="M26 12 L16 22 L26 32" fill="none" stroke="#fff" stroke-width="2.5"/></svg>
</div>
<div class="abs hero-arrow" style="left:1086px">
  <svg width="44" height="44" viewBox="0 0 44 44"><path d="M18 12 L28 22 L18 32" fill="none" stroke="#fff" stroke-width="2.5"/></svg>
</div>

<h1 class="abs center hero-title">BOOKING IT ON A TRAVEL</h1>
<p class="abs center hero-sub">We all do online research before taking a vacation. Since some of us will spend hours<br>researching a trip before finally booking it on a travel website.</p>
<div class="abs btn" style="top:413px;left:341px;width:242px;height:47px">REGISTER NOW</div>
<div class="abs btn" style="top:413px;left:617px;width:241px;height:47px">BOOKING FOR TRAVEL</div>

<!-- Search -->
<div class="abs search"></div>
<div class="abs search-title">SINCE SOME OF US WILL SPEND HOURS RESEARCHING A TRIP BEFORE FINALLY BOOKING IT ON A TRAVEL</div>
<div class="abs field" style="left:171px">Date
  <svg width="14" height="14" viewBox="0 0 14 14"><rect x="1" y="2" width="12" height="11" fill="none" stroke="#bbb"/><line x1="1" y1="5" x2="13" y2="5" stroke="#bbb"/></svg></div>
<div class="abs field" style="left:351px">Location
  <svg width="12" height="16" viewBox="0 0 12 16"><path d="M6 15 C2 9 1 7 1 5.5 A5 5 0 0 1 11 5.5 C11 7 10 9 6 15Z" fill="#bbb"/><circle cx="6" cy="5.5" r="2" fill="#25272b"/></svg></div>
<div class="abs field" style="left:531px">Activity
  <svg width="14" height="14" viewBox="0 0 14 14"><circle cx="7" cy="7" r="6" fill="none" stroke="#bbb"/><path d="M4 8 Q7 11 10 8" fill="none" stroke="#bbb"/></svg></div>
<div class="abs field" style="left:711px">Cost
  <svg width="14" height="14" viewBox="0 0 14 14"><path d="M5 2 H9 L8 4 Q13 7 12 11 Q11 13 7 13 Q3 13 2 11 Q1 7 6 4Z" fill="#bbb"/></svg></div>
<div class="abs search-btn">SEARCH NOW</div>

<!-- Welcome -->
<h2 class="abs center sec-title" style="top:730px">WELCOME TO CORALPEAK TRAVEL</h2>
<p class="abs para" style="top:769px">It is a long established fact that a reader will be distracted by the readable content of a page when looking at its layout. The point of using Lorem Ipsum is that it has a more-or-less normal distribution of letters, as opposed to using 'Content here, content here', making it look like readable English. Many desktop publishing packages and web page editors...</p>
<div class="abs btn" style="top:862px;left:495px;width:210px;height:44px;font-size:18px">READ MORE INFO</div>
<div class="abs rule"></div>

<!-- Services -->
<h2 class="abs center sec-title" style="top:972px">OUR SERVICES</h2>
<p class="abs para" style="top:1011px">It is a long established fact that a reader will be distracted by the readable content of a page when looking at its layout. The point of using Lorem Ipsum is that it has a more-or-less normal distribution of letters, as opposed to using 'Content here...</p>

<div class="abs card" style="left:171px;background:var(--card-blue)">
  <h3>SERVICES 01</h3>
  <p>It is a long established fact that a reader will be distracted by the readable content of a page when looking at its layout. The point of using Lorem Ipsum is that it has a more-or-less normal distribution of letters, as opposed Content here...</p>
</div>
<div class="abs card" style="left:465px;background:var(--card-orange)">
  <h3>SERVICES 02</h3>
  <p>It is a long established fact that a reader will be distracted by the readable content of a page when looking at its layout. The point of using Lorem Ipsum is that it has a more-or-less normal distribution of letters, as opposed Content here...</p>
</div>
<div class="abs card" style="left:756px;background:var(--card-green)">
  <h3>SERVICES 03</h3>
  <p>It is a long established fact that a reader will be distracted by the readable content of a page when looking at its layout. The point of using Lorem Ipsum is that it has a more-or-less normal distribution of letters, as opposed Content here...</p>
</div>

<div class="abs badge" style="left:251px;border-color:var(--card-blue)">
  <svg width="96" height="96" viewBox="0 0 96 96">
    <ellipse cx="50" cy="54" rx="10" ry="17" fill="#3a3a3a"/>
    <ellipse cx="49" cy="73" rx="8" ry="7" fill="#3a3a3a"/>
    <circle cx="39" cy="31" r="4.5" fill="#3a3a3a"/>
    <circle cx="47" cy="28" r="3.5" fill="#3a3a3a"/>
    <circle cx="54" cy="29" r="3" fill="#3a3a3a"/>
    <circle cx="60" cy="32" r="2.6" fill="#3a3a3a"/>
    <circle cx="64" cy="37" r="2.3" fill="#3a3a3a"/>
  </svg>
</div>
<div class="abs badge" style="left:545px;border-color:var(--card-orange)">
  <svg width="96" height="96" viewBox="0 0 96 96">
    <path d="M24 52 L30 36 Q32 32 37 32 H59 Q64 32 66 36 L72 52 Q75 53 75 57 V66 H21 V57 Q21 53 24 52Z" fill="#3a3a3a"/>
    <path d="M32 50 L36 38 H60 L64 50Z" fill="#fff"/>
    <circle cx="31" cy="58" r="3" fill="#fff"/><circle cx="65" cy="58" r="3" fill="#fff"/>
    <rect x="24" y="66" width="9" height="7" fill="#3a3a3a"/><rect x="63" y="66" width="9" height="7" fill="#3a3a3a"/>
  </svg>
</div>
<div class="abs badge" style="left:836px;border-color:var(--card-green)">
  <svg width="96" height="96" viewBox="0 0 96 96">
    <path d="M40 22 Q36 27 40 32 Q44 37 40 42 M48 20 Q44 25 48 30 Q52 35 48 40 M56 22 Q52 27 56 32 Q60 37 56 42" fill="none" stroke="#3a3a3a" stroke-width="2.5"/>
    <path d="M20 52 H76 Q74 70 58 74 H38 Q22 70 20 52Z" fill="none" stroke="#3a3a3a" stroke-width="4"/>
    <path d="M28 58 Q48 64 68 58 M30 64 Q48 70 66 64" fill="none" stroke="#3a3a3a" stroke-width="2"/>
    <rect x="36" y="76" width="24" height="4" fill="#3a3a3a"/>
  </svg>
</div>

<!-- Testimonials -->
<div class="abs testimonials"></div>
<h2 class="abs center sec-title" style="top:1521px">TESTIMONIALS</h2>
<p class="abs para" style="top:1561px">It is a long established fact that a reader will be distracted by the readable content of a page when looking at its layout. The point of using Lorem Ipsum is that it has a more-or-less normal distribution of letters, as opposed to using 'Content here...</p>

<div class="abs t-arrow" style="left:112px">‹</div>
<div class="abs t-arrow" style="left:1074px">›</div>

<div class="abs t-card" style="left:171px">
  <div class="abs t-photo" role="img" aria-label="Portrait of a smiling customer at a laptop" style="background:linear-gradient(135deg,#4e7fb8 0%,#c79a7a 45%,#6e8fb3 100%)"></div>
  <div class="abs t-body">
    <div class="t-name">MARCO BELLINI</div>
    <div class="t-date">Posted on 27 mar 2014</div>
    <div class="t-text">It is a long established fact that a reader will be distracted by the readable content of a page when looking at its layout...</div>
  </div>
</div>
<div class="abs t-card" style="left:617px">
  <div class="abs t-photo" role="img" aria-label="Parent and child pointing out to sea on a beach" style="background:linear-gradient(180deg,#e3ecf4 0%,#7fb2d6 45%,#4f88b4 60%,#d9cdb8 100%)"></div>
  <div class="abs t-body">
    <div class="t-name">MARCO BELLINI</div>
    <div class="t-date">Posted on 27 mar 2014</div>
    <div class="t-text">It is a long established fact that a reader will be distracted by the readable content of a page when looking at its layout...</div>
  </div>
</div>

<!-- Contact band -->
<div class="abs contact"></div>
<div class="abs contact-text"><b>CONTACT US :</b> <i>It is a long established fact that a reader will be distracted by the readable content when looking at its layout...</i></div>
<div class="abs contact-btn">CONTACT NOW</div>

<!-- Newsletter -->
<div class="abs news" role="img" aria-label="Clear turquoise underwater scene with fish swimming"></div>
<h2 class="abs center sec-title" style="top:2012px;font-size:20px;font-weight:700">NEWSLETTER SIGNUP</h2>
<p class="abs news-para" style="top:2053px">It is a long established fact that a reader will be distracted by the readable content of a page when looking at its layout. The point of using Lorem Ipsum is that it has a more-or-less normal distribution of letters, as opposed to using 'Content here, content here...</p>
<div class="abs email">Your e-mail address...</div>
<div class="abs subscribe">
  <div class="ic"><svg width="12" height="12" viewBox="0 0 12 12"><path d="M1 1 L11 5 L6 6 L5 11Z" fill="#fff"/></svg></div>
  <span>Subscribe</span>
</div>

<div class="abs social" style="left:411px;background:#2e5aa8"></div>
<div class="abs social" style="left:467px;background:#3aa3dc"></div>
<div class="abs social" style="left:522px;background:#1f74ad"></div>
<div class="abs social" style="left:577px;background:#f0a11f"></div>
<div class="abs social" style="left:633px;background:#d5272d"></div>
<div class="abs social" style="left:688px;background:#2f2f2f"></div>
<div class="abs social" style="left:745px;background:#d9262e"></div>

<div class="abs foot-rule"></div>
<p class="abs center copyright">© 2014, CoralPeak Travel. All Rights Reserved.</p>

</body>
</html>
```